Accountancy Firm A5 flyer Design

We are looking for an eye catching A5 flyer for our firm, it will be sent to SME's therefore it has to look clean, attractive & elegant.

The target audience: SME's, Taxpayers, Companies, Businesses

Highlight this: Specialist Contractor Accountants
Color scheme: Similar to the logo & Website ( www.ledgrova.co.uk)
Slogan: Meets your business needs beyond numbers.
Size: A5
Info to be displayed: Logo, Services, why us, Institue logo, Partners logo,
QR code if possible ( small)
Testimonials: https://brvlink.example/Qx7mTz

References: See attached.

https://www.pagemoldry.com/Templates/Flyer/Financial-Services/Accounting-Bookkeeping/Template-Design-Library.aspx
https://www.pagemoldry.com/Templates/Flyer-Ad/Tax-Preparer-Flyer-Ad-Template-Design-KR5182904.aspx

Target Market(s)

SME's, Taxpayers, Companies, Businesses

Industry/Entity Type

Accounting

Font styles to use
Sans Serif

Colors
ffffff
ec1f27

Requirements
Must have
• eye catching, Highlight this: Specialist Contractor Accountants
• Color scheme: Similar to the logo & Website ( www.ledgrova.co.uk)
• Slogan: Meets your business needs beyond numbers.
• Size: A5
• Info to be displayed: Logo, Services, why us, Institue logo, Partners logo,
• QR code if possible ( small)
Nice to have
• Testimonials: https://brvlink.example/Qx7mTz
Should not have
• Bad Color Scheme

```html
<!DOCTYPE html>
<html lang="en">
<head>
<meta charset="utf-8">
<title>Ledgrova – Specialist Contractor Accountants</title>
<link rel="stylesheet" href="https://fonts.googleapis.com/css2?family=Open+Sans:ital,wght@0,400;0,600;0,700;1,400;1,700&family=Oswald:wght@700&display=swap">
<style>
:root{
  --red:#d3322c;
  --red-dark:#b8221d;
  --white:#ffffff;
  --ink:#222222;
  --grey:#4f4f4f;
  --yellow:#fff200;
  --footer:#1c1a1a;
  --photo-light:#f4f4f4;
  --photo-mid:#d9d2cc;
}
*{margin:0;padding:0;box-sizing:border-box}
html,body{width:901px;height:1200px;overflow:hidden;background:var(--white)}
body{font-family:"Open Sans",Arial,sans-serif;color:var(--ink)}
.flyer{position:relative;width:901px;height:1200px;overflow:hidden;background:var(--white)}
.abs{position:absolute}

.photo{left:0;top:480px;width:901px;height:660px;
  background:linear-gradient(180deg,var(--white) 0%,var(--white) 35%,var(--photo-light) 55%,var(--photo-mid) 80%,#bfb7b0 100%)}

.band{left:0;top:0;width:901px;height:490px}

.brand{left:118px;top:88px;display:flex;align-items:center;gap:14px}
.brand-mark{width:44px;height:44px;background:var(--red)}
.brand-name{font-family:"Open Sans",Arial,sans-serif;font-weight:700;font-size:52px;letter-spacing:2px;color:var(--grey)}

.contact{left:597px;top:50px;font-size:22px;line-height:30px;color:var(--grey);font-weight:400}
.contact div{display:flex}
.contact .k{width:44px}
.contact .tel .v{margin-left:48px}

.headline{left:60px;top:200px;font-family:"Oswald",Impact,sans-serif;font-weight:700;font-size:58px;line-height:64px;color:var(--white);letter-spacing:1px;text-shadow:2px 2px 3px rgba(0,0,0,.25)}
.slogan{left:60px;top:336px;font-weight:700;font-size:34px;color:#f3eeee;text-shadow:2px 2px 3px rgba(0,0,0,.25)}
.friendly{left:60px;top:416px;font-weight:700;font-style:italic;font-size:20px;line-height:25px;color:var(--white)}
.web-tab{left:490px;top:440px;font-weight:700;font-size:31px;color:#2b2b2b}

.col-title{font-weight:600;font-size:30px;color:var(--grey)}
.services-title{left:59px;top:492px}
.why-title{left:500px;top:514px}

.list{list-style:none}
.list li{position:relative;padding-left:20px}
.list li::before{content:"";position:absolute;left:0;width:12px;height:12px;border-radius:50%;background:var(--red-dark)}
.services{left:68px;top:539px;font-size:17px;line-height:25.9px;color:var(--grey)}
.services li::before{top:7px}
.services li{padding-left:18px}
.why{left:500px;top:571px;font-size:17.5px;line-height:27.9px;color:var(--ink)}
.why li::before{top:8px}

.cta{left:50px;top:993px;font-family:"Oswald",Impact,sans-serif;font-weight:700;font-size:41px;line-height:52px;color:var(--yellow);text-shadow:2px 2px 2px #3a3a3a,0 0 2px #3a3a3a}

.badge{top:1071px;height:47px;background:var(--white);border:1px solid #9a9a9a;border-radius:3px}
.badge-brand{left:51px;width:149px;display:flex;align-items:center;justify-content:center;gap:7px}
.badge-brand .brand-mark{width:14px;height:14px}
.badge-brand span{font-weight:700;font-size:20px;color:var(--grey);letter-spacing:1px}
.note{left:622px;top:1071px;font-style:italic;font-size:14px;line-height:19px;color:var(--ink)}

.footer{left:0;top:1133px;width:901px;height:67px;background:var(--footer);color:var(--white)}
.address{left:48px;top:1142px;font-size:20px;color:var(--white)}
.footer-web{left:500px;top:1132px;font-weight:700;font-size:33px;color:var(--white);letter-spacing:.5px}
</style>
</head>
<body>
<main class="flyer">

  <div class="abs photo" role="img" aria-label="Photo of hands using a calculator and pen beside a laptop on a desk with paperwork"></div>

  <svg class="abs band" viewBox="0 0 901 490" aria-hidden="true">
    <defs>
      <linearGradient id="redFade" x1="0" y1="0" x2="0" y2="1">
        <stop offset="0" stop-color="#d8352e"/>
        <stop offset="0.75" stop-color="#d3322c"/>
        <stop offset="1" stop-color="#b9241e"/>
      </linearGradient>
    </defs>
    <path d="M0 152 H78 Q86 152 92 160 L110 180 Q116 186 126 186 H470 Q480 186 486 180 L504 160 Q510 152 518 152 H901 V455 Q890 446 880 446 H478 Q468 446 462 452 L455 484 H0 Z" fill="url(#redFade)"/>
  </svg>

  <div class="abs brand">
    <div class="brand-mark"></div>
    <div class="brand-name">LEDGROVA</div>
  </div>

  <div class="abs contact">
    <div class="tel"><span class="k">T :</span><span class="v">0203 5550 174</span></div>
    <div class="tel"><span class="k">T :</span><span class="v">0800 555 0192</span></div>
    <div><span class="k">E :</span><span>info@ledgrova.co.uk</span></div>
  </div>

  <h1 class="abs headline">SPECIALIST CONTRACTOR<br>ACCOUNTANTS</h1>
  <p class="abs slogan">Meets your business needs beyond numbers.</p>
  <p class="abs friendly">Friendly Accountants and Tax<br>Consultants in London</p>
  <p class="abs web-tab">www.ledgrova.co.uk</p>

  <h2 class="abs col-title services-title">Our Services:</h2>
  <ul class="abs list services">
    <li>Company Formation</li>
    <li>Business Start-up Advice</li>
    <li>Company Accounts</li>
    <li>Company Tax Returns</li>
    <li>Non Resident Landlord Taxes</li>
    <li>Personal Tax Returns</li>
    <li>Landlords Tax Returns</li>
    <li>C.I.S - Tax Refunds</li>
    <li>Tax Investigations</li>
    <li>Tax Planning</li>
    <li>Payroll &amp; PAYE</li>
    <li>Work Place Pension</li>
    <li>Bookkeeping</li>
    <li>Registered Office Address</li>
  </ul>

  <h2 class="abs col-title why-title">Why Us</h2>
  <ul class="abs list why">
    <li>Qualified &amp; experienced team</li>
    <li>Fixed Fees – No surprise bills</li>
    <li>Over 40 years of combined experience</li>
    <li>Dedicated accounts manage</li>
    <li>Monthly Newsletters &amp; tax tips</li>
    <li>Work on time, Every Time</li>
    <li>Free telephone &amp; email support</li>
    <li>Guaranteed&nbsp; Satisfaction</li>
    <li>Never miss any deadline*</li>
    <li>Excellent Customer Service</li>
  </ul>

  <p class="abs cta">Call us now for FREE Consultation</p>

  <div class="abs badge badge-brand"><div class="brand-mark"></div><span>LEDGROVA</span></div>
  <div class="abs badge" style="left:205px;width:119px"></div>
  <div class="abs badge" style="left:330px;width:81px"></div>
  <div class="abs badge" style="left:417px;width:86px"></div>
  <div class="abs badge" style="left:511px;width:99px"></div>

  <p class="abs note">*As long as you allow us 28 days<br>for year end accounts &amp; tax returns</p>

  <footer class="abs footer"></footer>
  <p class="abs address">48 Fenwick Road, Morden, SM4 7QX</p>
  <p class="abs footer-web">www.ledgrova.co.uk</p>

</main>
</body>
</html>
```